Christmas Lights Tour - London Coach Tour with Cheese & Wine

Brambleford Coach Services Ltd require a flyer to be mailed and posted online for customers wishing to book Christmas Packages with us. This package will be aimed at Adults only. The sleek design will be festive and eyecatching. Our company holds annual Christmas Light Tours around London. Supplying cheese and wine bundles and further catering if required. The tour will last 3 hours in total.

Target Market(s)

Adults, Teachers, Christmas Party, Church Groups

Industry/Entity Type

Party Planning

Requirements
Must have
• Festive, Sleek,
Should not have
• Cheesy Images

```html
<!DOCTYPE html>
<html lang="en">
<head>
<meta charset="utf-8">
<title>Christmas Light Tours around London – Flyer</title>
<link rel="stylesheet" href="https://fonts.googleapis.com/css2?family=Montserrat:wght@300;400;500;600&family=Kaushan+Script&display=swap">
<style>
  :root {
    --stage: #141315;
    --card: #232124;
    --maroon: #7a2227;
    --gold: #c9a24a;
    --white: #ffffff;
    --soft: #e6e1e2;
    --brand-accent: #e8782a;
  }
  * { box-sizing: border-box; margin: 0; padding: 0; }
  html, body { width: 1200px; height: 1200px; overflow: hidden; background: var(--stage); }
  body { position: relative; font-family: "Montserrat", sans-serif; color: var(--white); }

  .flyer {
    position: absolute; left: 100px; width: 1000px; height: 540px;
    background: var(--card); overflow: hidden;
  }
  .flyer--front { top: 40px; }
  .flyer--back { top: 620px; }

  .band {
    position: absolute; left: 0; right: 0; bottom: 0; height: 170px;
    background: var(--maroon); border-top: 2px solid var(--gold); z-index: 3;
  }

  .brand {
    position: absolute; display: flex; align-items: center; gap: 10px;
    font-weight: 600; font-size: 30px; letter-spacing: 1px; color: var(--white);
  }
  .brand__dot { width: 14px; height: 14px; border-radius: 50%; background: var(--brand-accent); }

  /* front */
  .title { position: absolute; left: 90px; top: 120px; line-height: 1; }
  .title__script { font-family: "Kaushan Script", cursive; font-size: 66px; display: block; margin-bottom: 8px; }
  .title__line { display: block; font-size: 44px; font-weight: 500; margin-bottom: 6px; }
  .title__line--light { font-weight: 300; }

  .photo {
    position: absolute; left: 540px; top: -60px; width: 480px; height: 480px;
    border-radius: 50%;
    background: radial-gradient(circle at 75% 35%, #b0245a 0%, #4a1a33 30%, #1c1520 60%, #3a3436 100%);
    z-index: 1;
  }
  .rings { position: absolute; left: 500px; top: -100px; width: 560px; height: 560px; z-index: 2; }

  .slogan { position: absolute; left: 90px; top: 40px; }
  .slogan__head { font-size: 26px; font-weight: 600; margin-bottom: 6px; }
  .slogan__body { font-size: 17px; font-weight: 300; line-height: 1.4; color: var(--soft); }
  .flyer--front .brand { right: 70px; top: 62px; }

  /* back */
  .flyer--back .brand { right: 70px; top: 40px; font-size: 28px; }
  .mini-title { position: absolute; left: 90px; top: 70px; line-height: 1; }
  .mini-title__script { font-family: "Kaushan Script", cursive; font-size: 40px; }
  .mini-title__rest { display: block; font-size: 19px; font-weight: 400; margin-top: 4px; }
  .mini-title__rest b { font-weight: 600; }

  .detail { position: absolute; width: 340px; font-size: 16px; font-weight: 300; line-height: 1.3; color: var(--soft); }
  .detail h3 { font-size: 22px; font-weight: 600; color: var(--white); margin-bottom: 4px; }
  .detail p + p { margin-top: 6px; }
  .detail ul { list-style: none; margin-top: 4px; padding-left: 14px; }
  .detail li::before { content: "•"; margin-right: 14px; }
  .detail--left { left: 90px; top: 160px; }
  .detail--right { left: 560px; top: 110px; }

  .contact { position: absolute; left: 90px; top: 34px; }
  .contact h3 { font-size: 26px; font-weight: 600; margin-bottom: 10px; }
  .contact__row { display: flex; align-items: center; gap: 10px; font-size: 24px; font-weight: 500; }
  .email { position: absolute; left: 430px; top: 82px; display: flex; align-items: center; gap: 12px; font-size: 22px; font-weight: 500; }
  .social { position: absolute; right: 70px; top: 34px; display: flex; gap: 22px; }
  .social span { width: 34px; height: 34px; border-radius: 50%; background: var(--white); }
  .note { position: absolute; left: 430px; top: 128px; font-size: 12px; font-weight: 300; color: var(--soft); }
</style>
</head>
<body>

<section class="flyer flyer--front">
  <h1 class="title">
    <span class="title__script">Christmas</span>
    <span class="title__line">Light Tours</span>
    <span class="title__line title__line--light">around</span>
    <span class="title__line">LONDON</span>
  </h1>

  <div class="photo" role="img" aria-label="Photo of a coach at night on a London road with an illuminated observation wheel"></div>
  <svg class="rings" viewBox="0 0 560 560" aria-hidden="true">
    <circle cx="282" cy="278" r="262" fill="none" stroke="#c9a24a" stroke-width="2"/>
    <circle cx="270" cy="290" r="250" fill="none" stroke="#c9a24a" stroke-width="1.5" opacity="0.8"/>
  </svg>

  <div class="band">
    <div class="slogan">
      <p class="slogan__head">Experience slogan here</p>
      <p class="slogan__body">Lorem ipsum dolor sit amet, consectetuer adipiscing elit.<br>Aenean commodo ligula eget dolor. Aenean massa.</p>
    </div>
    <div class="brand"><span class="brand__dot"></span>Brambleford</div>
  </div>
</section>

<section class="flyer flyer--back">
  <div class="brand"><span class="brand__dot"></span>Brambleford</div>

  <h2 class="mini-title">
    <span class="mini-title__script">Christmas</span>
    <span class="mini-title__rest"><b>Light Tours</b> around <b>LONDON</b></span>
  </h2>

  <div class="detail detail--left">
    <h3>Tour Deatil Here</h3>
    <p>Lorem ipsum dolor sit amet, consectetuer adipiscing elit. Aenean commodo ligula eget dolor. Aenean massa.</p>
    <p>Lorem ipsum dolor sit amet, consectetuer adipiscing elit. Aenean commodo ligula eget dolor. Aenean massa.</p>
  </div>

  <div class="detail detail--right">
    <h3>Tour Deatil Here</h3>
    <p>Lorem ipsum dolor sit amet, consectetuer adipiscing elit. Aenean commodo ligula eget dolor. Aenean massa.</p>
    <ul>
      <li>Lorem ipsum dolor</li>
      <li>Lorem ipsum dolor</li>
      <li>Lorem ipsum dolor</li>
      <li>Lorem ipsum dolor</li>
    </ul>
  </div>

  <div class="band">
    <div class="contact">
      <h3>Contact Deatil Here</h3>
      <div class="contact__row">
        <svg width="22" height="22" viewBox="0 0 24 24" aria-hidden="true"><path fill="#fff" d="M6.6 10.8a15.1 15.1 0 0 0 6.6 6.6l2.2-2.2a1 1 0 0 1 1-.25 11.4 11.4 0 0 0 3.6.57 1 1 0 0 1 1 1V20a1 1 0 0 1-1 1A17 17 0 0 1 3 4a1 1 0 0 1 1-1h3.5a1 1 0 0 1 1 1c0 1.25.2 2.45.57 3.57a1 1 0 0 1-.25 1z"/></svg>
        0208 555 0142
      </div>
    </div>
    <div class="email">
      <svg width="24" height="18" viewBox="0 0 24 18" aria-hidden="true"><rect x="1" y="1" width="22" height="16" fill="#fff"/><path d="M1 1l11 9 11-9" fill="none" stroke="#7a2227" stroke-width="2"/></svg>
      info@brambleford-coaches.co.uk
    </div>
    <div class="social" aria-label="Social media"><span></span><span></span></div>
    <p class="note">Call Brambleford Coaches today for coach hire services from professional service providers in London.</p>
  </div>
</section>

</body>
</html>
```